new ownership of a business

Tax & accounting firm including payroll processing, business consulting, bookkeeping
I am a new owner and want to inform current clients I want the announcement to be subtle. something like "same friendly faces, brand new name" the name is going from "Warren T. Pickles, CPA, PC" to "Pickles Danvers & Associates, LLC" I would like to emphasize a little on the Danvers part of the name. I would like the words "Tax Accountants" below the name.
Accounting

```html
<!DOCTYPE html>
<html lang="en">
<head>
<meta charset="utf-8">
<title>Pickles Danvers &amp; Associates — New Name Announcement</title>
<link href="https://fonts.googleapis.com/css2?family=Questrial&family=Cinzel:wght@700;800&family=Arimo:wght@400;700&display=swap" rel="stylesheet">
<style>
  :root {
    --ink: #222226;
    --navy: #1e1b5e;
    --royal: #2e3192;
    --sky: #2a6ab5;
    --band-light: #2a78bf;
    --band-dark: #0e3f7a;
    --stripe: #1c2a6b;
    --paper-top: #dde4ee;
    --paper-bottom: #ffffff;
    --white: #ffffff;
  }
  html, body {
    margin: 0;
    padding: 0;
    width: 1200px;
    height: 958px;
    overflow: hidden;
  }
  .flyer {
    position: relative;
    width: 1200px;
    height: 958px;
    background: linear-gradient(180deg, var(--paper-top) 0%, var(--paper-bottom) 45%, #f3f6fa 100%);
    font-family: "Arimo", Arial, sans-serif;
    color: var(--ink);
    overflow: hidden;
  }
  .centered {
    position: absolute;
    left: 0;
    width: 1200px;
    text-align: center;
    margin: 0;
  }
  .tagline {
    top: 50px;
    font-family: "Questrial", sans-serif;
    font-size: 36px;
    letter-spacing: 2.5px;
    text-transform: uppercase;
  }
  .transition-note {
    top: 112px;
    font-family: "Arimo", sans-serif;
    font-size: 29px;
    padding-left: 0;
  }
  .old-name {
    top: 182px;
    font-family: "Arimo", sans-serif;
    font-weight: 700;
    font-size: 38px;
    color: var(--royal);
  }
  .connector {
    top: 240px;
    font-size: 29px;
  }
  .new-name {
    top: 282px;
    font-family: "Cinzel", serif;
    font-weight: 800;
    font-size: 54px;
    color: var(--navy);
    letter-spacing: 0.5px;
    line-height: 1;
  }
  .new-name .emphasis {
    font-size: 70px;
  }
  .descriptor {
    top: 364px;
    font-family: "Questrial", sans-serif;
    font-size: 42px;
    color: var(--sky);
    letter-spacing: 2px;
  }
  .photo-handshake {
    position: absolute;
    left: 52px;
    top: 424px;
    width: 494px;
    height: 420px;
    border-radius: 50%;
    background: radial-gradient(ellipse at 45% 55%, #e8c8b0 0%, #b7a7a0 35%, #6b7f97 70%, #c9d3df 100%);
    box-shadow: 0 0 0 4px rgba(255,255,255,0.8);
  }
  .services {
    position: absolute;
    left: 640px;
    top: 458px;
    margin: 0;
    padding: 0;
    list-style: none;
  }
  .service {
    display: flex;
    align-items: center;
    height: 81px;
    font-size: 44px;
    color: var(--ink);
  }
  .service svg {
    width: 46px;
    height: 46px;
    margin-right: 22px;
    flex: none;
  }
  .footer-wave {
    position: absolute;
    left: 0;
    top: 0;
    width: 1200px;
    height: 958px;
  }
  .contact {
    position: absolute;
    color: var(--white);
    font-family: "Arimo", sans-serif;
    display: flex;
    align-items: center;
    margin: 0;
  }
  .contact svg { flex: none; }
  .contact-phone {
    right: 38px;
    top: 858px;
    font-size: 35px;
    font-weight: 700;
    letter-spacing: 1px;
  }
  .contact-phone svg { width: 36px; height: 36px; margin-right: 8px; }
  .contact-email {
    left: 62px;
    top: 906px;
    font-size: 25px;
  }
  .contact-email svg { width: 30px; height: 22px; margin-right: 10px; }
  .contact-web {
    right: 38px;
    top: 906px;
    font-size: 25px;
  }
  .contact-web svg { width: 20px; height: 20px; margin-right: 6px; }
</style>
</head>
<body>
<main class="flyer">
  <p class="centered tagline">Same friendly faces, brand new name</p>
  <p class="centered transition-note">the name is going from</p>
  <p class="centered old-name">Warren T. Pickles, CPA, PC</p>
  <p class="centered connector">to</p>
  <h1 class="centered new-name">Pickles <span class="emphasis">Danvers</span> &amp; Associates, LLC</h1>
  <p class="centered descriptor">Tax Accountants</p>

  <div class="photo-handshake" role="img" aria-label="Photo of two business people shaking hands in an office"></div>

  <ul class="services">
    <li class="service">
      <svg viewBox="0 0 46 46" aria-hidden="true">
        <circle cx="23" cy="23" r="20" fill="#2a6ab5"/>
        <path d="M23 23 L23 3 A20 20 0 0 1 42 17 Z" fill="#7cc2f0"/>
        <path d="M23 23 L8 36 A20 20 0 0 1 4 19 Z" fill="#3fa34d"/>
      </svg>
      Tax &amp; Accounting
    </li>
    <li class="service">
      <svg viewBox="0 0 46 46" aria-hidden="true">
        <rect x="4" y="6" width="11" height="36" fill="#2e3192"/>
        <rect x="17" y="6" width="11" height="36" fill="#d62b2b"/>
        <rect x="30" y="6" width="11" height="36" fill="#d62b2b"/>
        <rect x="6" y="12" width="7" height="6" fill="#fff"/>
        <rect x="19" y="12" width="7" height="6" fill="#fff"/>
        <rect x="32" y="12" width="7" height="6" fill="#fff"/>
      </svg>
      Bookkeeping service
    </li>
    <li class="service">
      <svg viewBox="0 0 46 46" aria-hidden="true">
        <rect x="4" y="32" width="7" height="10" fill="#2a6ab5"/>
        <rect x="14" y="26" width="7" height="16" fill="#2a6ab5"/>
        <rect x="24" y="22" width="7" height="20" fill="#2a6ab5"/>
        <rect x="34" y="16" width="7" height="26" fill="#2a6ab5"/>
        <polyline points="4,24 16,16 26,18 40,6" fill="none" stroke="#3fa34d" stroke-width="3"/>
        <polygon points="42,3 42,11 35,5" fill="#3fa34d"/>
      </svg>
      Business consulting
    </li>
    <li class="service">
      <svg viewBox="0 0 46 46" aria-hidden="true">
        <polygon points="4,30 30,16 42,24 16,38" fill="#6c9a4a"/>
        <polygon points="4,26 30,12 42,20 16,34" fill="#a9cf7f"/>
        <polygon points="16,34 42,20 42,24 16,38" fill="#4d7a34"/>
        <ellipse cx="23" cy="23" rx="5" ry="3" fill="#6c9a4a"/>
      </svg>
      Payroll processing
    </li>
  </ul>

  <svg class="footer-wave" viewBox="0 0 1200 958" aria-hidden="true">
    <defs>
      <linearGradient id="bandFill" x1="0" y1="0" x2="1" y2="0">
        <stop offset="0" stop-color="var(--band-light)"/>
        <stop offset="1" stop-color="var(--band-dark)"/>
      </linearGradient>
      <linearGradient id="silverSwoosh" x1="0" y1="0" x2="1" y2="0">
        <stop offset="0" stop-color="#b8c0c8"/>
        <stop offset="1" stop-color="#ffffff" stop-opacity="0"/>
      </linearGradient>
    </defs>
    <path d="M0 838 C220 858 420 868 620 858 C500 870 260 872 0 862 Z" fill="url(#silverSwoosh)"/>
    <path d="M0 876 C320 884 720 838 1200 800 L1200 958 L0 958 Z" fill="url(#bandFill)"/>
    <path d="M560 862 C800 822 1000 798 1200 780 L1200 812 C1000 822 800 842 560 862 Z" fill="var(--stripe)"/>
  </svg>

  <p class="contact contact-phone">
    <svg viewBox="0 0 36 36" aria-hidden="true">
      <circle cx="18" cy="18" r="16" fill="none" stroke="#fff" stroke-width="2"/>
      <path d="M12 9 C10 11 10 15 13 20 C16 25 20 27 23 27 L25 24 L21 21 L19 23 C17 22 14 18 14 16 L16 14 L14 9 Z" fill="#fff"/>
    </svg>
    123. 456. 7890
  </p>
  <p class="contact contact-email">
    <svg viewBox="0 0 30 22" aria-hidden="true">
      <rect x="1" y="1" width="28" height="20" fill="#fff"/>
      <polyline points="1,1 15,12 29,1" fill="none" stroke="#1a5fa0" stroke-width="2"/>
    </svg>
    name@PicklesDanvers&amp;Associates.com
  </p>
  <p class="contact contact-web">
    <svg viewBox="0 0 20 20" aria-hidden="true">
      <circle cx="10" cy="10" r="8.5" fill="none" stroke="#fff" stroke-width="1.6"/>
      <ellipse cx="10" cy="10" rx="3.5" ry="8.5" fill="none" stroke="#fff" stroke-width="1.4"/>
      <line x1="1.5" y1="10" x2="18.5" y2="10" stroke="#fff" stroke-width="1.4"/>
    </svg>
    www.PicklesDanvers&amp;Associates.com
  </p>
</main>
</body>
</html>
```